Locksmith SmartPhone Web Design Project

I am a locksmith and focus on customers that use their smart phones to find me. I have a static web page that I created myself but it is horrible. See for yourself at www.brevalkeyworks.com.au

I want a cross-platform static site that simply shows the information and with the ability to change minor items like pricing. I want it to be compelling in its look and feel (not overwhelming) but simple. It must have a; click to call button; the ability to install a hit counter from pagetallyo.com; payment information just like the current graphic of card/cash/quidlo (orla/brixalonte only).

This will be hosted on my own server.
Updates

Hello Designers,

I have updated the brief in the must have and nice to have fields.

Thank you all,

Tom.

Hello to all Designers,

There is about 9 days left before the deadline. The overall level of competition is extremely high and I would like to thank all the designers who have submitted so far, 27 submissions in total so far. Excellent work.

If you have submitted already and wish to provide new designs, I am keen to see them. 

Hi guys, time is almost up. Please submit any new designs that you may have. The quality has been excellent so far.

Tom.

Target Market(s)

People who are locked out of their house/shop/office etc.

Industry/Entity Type

Locksmith

Requirements
Must have
• click to call button
hit counter from pagetallyo
payment graphic card/cash/quidlo (orla/brixalonte only)
cross platform compatibility smartphone/phablet
Single column page preferable, can have two columns.
Nice to have
• When the page loads regardless of the mobile device, all info should be presented. In other words no vertical or horizontal scroll bars.
Should not have
• hidden code, advertising, credits etc

```html
<!DOCTYPE html>
<html lang="en">
<head>
<meta charset="utf-8">
<title>Breval Keyworks</title>
<link href="https://fonts.googleapis.com/css2?family=Arimo:wght@400;700&family=Signika:wght@600&display=swap" rel="stylesheet">
<style>
:root{
  --page:#1c2436;
  --panel:#262f45;
  --panel-edge:#3a4868;
  --header-top:#2a3a66;
  --header-bottom:#14213f;
  --white:#ffffff;
  --heading:#7c98e8;
  --rule:#3b8ad0;
  --rule-soft:#6a7fa8;
  --body:#c9ced8;
  --muted:#9aa3b5;
  --button-top:#8fc2f5;
  --button-bottom:#4a8fe0;
  --button-text:#1a2440;
}
*{margin:0;padding:0;box-sizing:border-box}
html,body{width:1200px;height:3748px;overflow:hidden;background:var(--page)}
body{position:relative;font-family:'Arimo',Arial,sans-serif}
.masthead{position:absolute;left:8px;top:8px;width:1184px;height:604px;
  background:linear-gradient(180deg,var(--header-top),var(--header-bottom));
  border:3px solid var(--panel-edge);text-align:center;color:var(--white)}
.masthead .brand{font-weight:700;font-size:150px;line-height:172px;margin-top:40px}
.masthead .offer{font-weight:700;font-size:74px;line-height:84px;margin-top:22px}
.content{position:absolute;left:8px;top:624px;width:1184px;height:3124px;
  background:var(--panel);border:3px solid var(--panel-edge);border-bottom:none}
.section-title{position:absolute;left:68px;font-family:'Signika',sans-serif;font-weight:600;
  font-size:64px;color:var(--heading);letter-spacing:1px}
.rule{position:absolute;left:68px;width:1060px;height:4px}
.rule.soft{background:var(--rule-soft)}
.rule.blue{background:var(--rule)}
.intro{position:absolute;left:174px;top:255px;width:940px;font-size:49px;line-height:61px;color:var(--body)}
.services{position:absolute;left:212px;top:485px;list-style:none;color:var(--body);font-size:53px;line-height:72px}
.services li{position:relative;padding-left:56px}
.services li::before{content:"\2192";position:absolute;left:0;top:-4px;font-size:40px;color:var(--body)}
.payments{position:absolute;left:82px;top:1255px;display:flex;gap:8px}
.pay{width:200px;height:120px;background:#f4f4f4;border:3px solid #9aa3b5;display:flex;
  align-items:center;justify-content:center;font-weight:700;font-size:34px;color:#1a2440}
.pay.cash{background:linear-gradient(135deg,#7da35a,#c98a4a 50%,#5b8fc0)}
.call-button{position:absolute;left:68px;top:1630px;width:776px;height:186px;
  background:linear-gradient(180deg,var(--button-top),var(--button-bottom));
  border:4px solid #a8c8ee;box-shadow:0 8px 10px rgba(0,0,0,.35);
  display:flex;align-items:center;justify-content:center;text-decoration:none;
  font-weight:700;font-size:42px;color:var(--button-text)}
.phone{position:absolute;left:68px;top:1935px;font-size:70px;color:var(--white)}
.phone span{color:var(--muted)}
.hours{position:absolute;left:68px;top:2020px;font-weight:700;font-size:49px;color:var(--muted)}
.like{position:absolute;left:68px;top:2385px;display:flex;gap:84px;align-items:flex-start}
.like-button{width:178px;height:84px;background:linear-gradient(180deg,#f4f4f4,#d6d6d6);
  border:3px solid #9a9a9a;border-radius:6px;display:flex;align-items:center;justify-content:center;
  font-size:38px;color:#333}
.like-text{width:790px;font-size:39px;line-height:52px;color:var(--muted);margin-top:2px}
.like-text b{color:var(--white);font-weight:400}
</style>
</head>
<body>
<header class="masthead">
  <div class="brand">Breval<br>Keyworks®</div>
  <div class="offer">LOCKED OUT? $150 GETS<br>YOU IN. EASY!</div>
</header>

<main class="content">
  <h2 class="section-title" style="top:75px">OUR SERVICES</h2>
  <div class="rule soft" style="top:190px"></div>
  <p class="intro">Breval Keyworks provide a range of Locksmith services for both home and business including:</p>
  <ul class="services">
    <li>Locked Out</li>
    <li>Change of Keys</li>
    <li>Make new Keys</li>
    <li>Restricted Key Systems</li>
    <li>Automotive Locksmiths</li>
    <li>Services Access Control</li>
    <li>Safes Services</li>
    <li>Alarm Systems</li>
  </ul>

  <h2 class="section-title" style="top:1075px">PAYMENT OPTIONS</h2>
  <div class="rule blue" style="top:1232px"></div>
  <div class="payments">
    <div class="pay">brixalonte</div>
    <div class="pay">orla</div>
    <div class="pay cash" role="img" aria-label="Banknotes photo for cash payment"></div>
    <div class="pay">quidlo</div>
  </div>

  <h2 class="section-title" style="top:1445px">CONTACT US</h2>
  <div class="rule blue" style="top:1576px"></div>
  <a class="call-button" href="tel:0491570118">click to call now</a>
  <p class="phone"><span>Ph:</span> 0491 570 118</p>
  <p class="hours">Available 24 hours a day, 7 days a week</p>

  <h2 class="section-title" style="top:2212px">LIKE US ON CIRCLEBOOK</h2>
  <div class="rule blue" style="top:2333px"></div>
  <div class="like">
    <div class="like-button">Like</div>
    <p class="like-text">3,666,997 people like this. <b>Sign Up</b> to see what your friends like.</p>
  </div>
</main>
</body>
</html>
```